Business Card Design Project

We consult with hotels on setting rates and maximizing a revenue strategy

Industry/Entity Type

Business

Contact Information for Business Card

I am not sure what I want. Our company offers high level consulting to hotels around the country but we are also laid back. I would like something that is professional but also shows the laid back side

```html
<!DOCTYPE html>
<html lang="en">
<head>
<meta charset="utf-8">
<title>Harborline Revenue Management Solutions – Business Card</title>
<link rel="stylesheet" href="https://fonts.googleapis.com/css2?family=Open+Sans:wght@400;600;700&display=swap">
<style>
  :root {
    --page-bg: #e6e4e1;
    --teal: #2f8f8a;
    --teal-light: #a9d4d8;
    --teal-pale: #e9f4f5;
    --brown: #3b2a23;
    --band-sub: #1d3d3b;
    --ink: #2a2a2a;
    --white: #ffffff;
  }
  * { margin: 0; padding: 0; box-sizing: border-box; }
  html, body {
    width: 1200px; height: 1001px; overflow: hidden;
    background: var(--page-bg);
    font-family: "Open Sans", Arial, sans-serif;
  }
  .stage {
    width: 1200px; height: 1001px;
    display: flex; justify-content: center; align-items: center; gap: 100px;
  }
  .card {
    width: 400px; height: 700px; position: relative; overflow: hidden;
    background: var(--white);
    box-shadow: 0 6px 18px rgba(0,0,0,0.18);
  }

  /* Name mark: plain name beside one plain square */
  .name-mark {
    display: flex; align-items: center; gap: 12px;
  }
  .name-mark-square {
    width: 28px; height: 28px; background: var(--teal); flex: none;
  }
  .name-mark-text {
    font-weight: 600; color: var(--brown); line-height: 1;
  }

  /* Back side */
  .card--back {
    background: linear-gradient(to bottom, var(--teal-light) 0%, var(--teal-pale) 55%, var(--white) 100%);
  }
  .back-url {
    position: absolute; top: 50px; left: 0; right: 0; text-align: center;
    font-weight: 700; font-size: 20px; color: var(--ink);
  }
  .card--back .name-mark {
    position: absolute; right: 30px; bottom: 60px;
  }
  .card--back .name-mark-text { font-size: 30px; }

  /* Front side */
  .front-top {
    height: 250px; display: flex; justify-content: center; align-items: center;
  }
  .card--front .name-mark-text { font-size: 36px; }
  .front-band {
    height: 110px; background: var(--teal); color: var(--white);
    display: flex; flex-direction: column; justify-content: center; align-items: center;
  }
  .band-name { font-size: 34px; font-weight: 400; letter-spacing: 1px; line-height: 1.1; }
  .band-sub { font-size: 14px; color: var(--band-sub); }
  .front-contact {
    height: 340px; background: var(--brown); color: var(--white);
    display: flex; flex-direction: column; align-items: center; padding-top: 60px;
    font-size: 17px; line-height: 1.9;
  }
  .contact-name { font-size: 20px; }
  .contact-title { margin-bottom: 6px; }
</style>
</head>
<body>
<main class="stage">
  <section class="card card--back">
    <p class="back-url">www.HarborlineRMS.com</p>
    <div class="name-mark">
      <span class="name-mark-square"></span>
      <span class="name-mark-text">Harborline</span>
    </div>
  </section>

  <section class="card card--front">
    <div class="front-top">
      <div class="name-mark">
        <span class="name-mark-square"></span>
        <span class="name-mark-text">Harborline</span>
      </div>
    </div>
    <div class="front-band">
      <span class="band-name">HARBORLINE</span>
      <span class="band-sub">Revenue Management Solutions LLC</span>
    </div>
    <div class="front-contact">
      <span class="contact-name">Dana Whitmore</span>
      <span class="contact-title">Regional Revenue Manager</span>
      <span>Office 555-014-2738</span>
      <span>Fax 555-014-6290</span>
      <span>danaw@HarborlineRMS.com</span>
    </div>
  </section>
</main>
</body>
</html>
```